Gently Paused for Quiet Renewal & Inner Housekeeping (guidebook) - needs a front and back bo

Can you use the two piece 3d mock up using the FRONT and the BACK.

And can you use the one piece with just the FRONT cover only.

Font styles to use
Sans Serif
Script
Other font styles liked:
• see font used on my amber HARBOR memoir

Colors
33a6d7
acd037
faa54b
f04a51
b8a5cd
85cae6
33b8a4
cadf82
fbee3f

Requirements
Must have
• Everything described in product description.

```html
<!DOCTYPE html>
<html lang="en">
<head>
<meta charset="utf-8">
<title>Gently Paused — A Guidebook</title>
<link rel="stylesheet" href="https://fonts.googleapis.com/css2?family=Open+Sans:wght@400;700;800&family=Permanent+Marker&family=Satisfy&display=swap">
<style>
  :root {
    --blue: #33a6d7;
    --green: #acd037;
    --orange: #faa54b;
    --coral: #f04a51;
    --lilac: #b8a5cd;
    --sky: #85cae6;
    --teal: #33b8a4;
    --lime: #cadf82;
    --yellow: #fbee3f;
    --paper: #dcdcdc;
    --ink: #1e1e22;
    --stamp-dark: #3a3c42;
    --stamp-red: #f2646b;
    --author-grey: #6f6f6f;
  }
  html, body {
    margin: 0;
    padding: 0;
    width: 840px;
    height: 1200px;
    overflow: hidden;
  }
  .cover {
    position: relative;
    width: 840px;
    height: 1200px;
    background: linear-gradient(180deg,
      var(--blue) 0%, var(--green) 16%, var(--yellow) 24%, var(--orange) 36%,
      var(--coral) 48%, #d97aa5 58%, var(--lilac) 66%, var(--sky) 78%,
      var(--teal) 86%, var(--lime) 93%, var(--yellow) 100%);
    font-family: "Open Sans", Arial, sans-serif;
  }
  .cover-face {
    position: absolute;
    inset: 8px;
    background: var(--paper);
    overflow: hidden;
  }
  .companion-line {
    position: absolute;
    top: 50px;
    left: 64px;
    right: 64px;
    display: flex;
    justify-content: space-between;
    font-size: 22px;
    letter-spacing: 0.2px;
    color: var(--ink);
  }
  .companion-book {
    position: absolute;
    left: 440px;
    top: 6px;
    width: 104px;
    height: 142px;
    transform: rotate(-8deg);
    background: linear-gradient(135deg, #f4f4f4, #c9c9c9);
    box-shadow: 2px 4px 8px rgba(0,0,0,0.25);
  }
  .stamp {
    position: absolute;
    left: 104px;
    top: 213px;
    width: 636px;
    height: 246px;
    transform: rotate(-14.6deg);
    border: 7px solid var(--stamp-dark);
    border-radius: 30px;
    box-sizing: border-box;
    text-align: center;
    font-weight: 800;
    line-height: 1;
  }
  .stamp-top {
    display: block;
    margin-top: 14px;
    font-size: 100px;
    color: var(--stamp-dark);
    letter-spacing: 2px;
  }
  .stamp-bottom {
    display: block;
    margin-top: 4px;
    font-size: 112px;
    color: var(--stamp-red);
    letter-spacing: 2px;
    -webkit-text-stroke: 3px var(--stamp-dark);
  }
  .subtitle {
    position: absolute;
    left: 200px;
    top: 520px;
    width: 460px;
    transform: rotate(-10deg);
    font-family: "Permanent Marker", cursive;
    font-size: 48px;
    line-height: 1.15;
    color: var(--ink);
  }
  .subtitle span { display: block; }
  .subtitle .indent-1 { padding-left: 40px; }
  .subtitle .indent-2 { padding-left: 10px; }
  .stones {
    position: absolute;
    left: 270px;
    top: 784px;
    width: 260px;
    height: 250px;
    border-radius: 45% 45% 40% 40%;
    background: radial-gradient(ellipse at 50% 45%, #b9b9b7 0%, #a4a4a2 45%, rgba(210,210,210,0) 75%);
  }
  .author {
    position: absolute;
    top: 1040px;
    left: 0;
    right: 0;
    text-align: center;
    font-size: 56px;
    font-weight: 400;
    color: var(--author-grey);
    letter-spacing: -1px;
  }
  .format-label {
    position: absolute;
    top: 1098px;
    left: 0;
    right: 0;
    text-align: center;
    font-family: "Satisfy", cursive;
    font-size: 52px;
    color: var(--coral);
  }
</style>
</head>
<body>
  <div class="cover">
    <div class="cover-face">
      <div class="companion-line">
        <span>A COMPANION TO AMBER HARBOR</span>
        <span>BY RL WHITFORD</span>
      </div>
      <div class="companion-book" role="img" aria-label="Small photo of the companion memoir amber HARBOR"></div>

      <h1 class="stamp">
        <span class="stamp-top">GENTLY</span>
        <span class="stamp-bottom">PAUSED</span>
      </h1>

      <p class="subtitle">
        <span>for Quiet Renewal</span>
        <span class="indent-1">&amp; Inner</span>
        <span class="indent-2">Housekeeping</span>
      </p>

      <div class="stones" role="img" aria-label="Photo of four smooth grey stones balanced in a stack"></div>

      <div class="author">RL WHITFORD</div>
      <div class="format-label">A Guidebook</div>
    </div>
  </div>
</body>
</html>
```